***Design a Nutritional Supplement Label for Bright Harvest!***

I have an existing label, I want to keep the logo but change the rest of the design. I am open to different creative ideas, but it needs to look appropriate for the shelves at Bright Harvest. This means it needs to look professional and premium, without being sterile and boring. I feel like my current label looks a little 1990s. You can play with the colors, font and design elements, while keeping the logo, descriptive text and the same layout. Feel free to take some bold chances. (You cannot change the font in the supplement facts section)

Font styles to use
Sans Serif

Colors

Designer to choose colors to be used in the design.

Requirements
Must have
• Keep the same text and layout. Keep the "Muscle Haven" logo as-is. DO NOT CHANGE THE LOGO!!

```html
<!DOCTYPE html>
<html lang="en">
<head>
<meta charset="UTF-8">
<title>Muscle Haven – Supplement Label</title>
<link rel="stylesheet" href="https://fonts.googleapis.com/css2?family=Roboto:wght@300;400;700;900&display=swap">
<style>
  :root {
    --canvas-bg: #f2f2f2;
    --silver-light: #f7f7f8;
    --silver-mid: #dcdde0;
    --silver-dark: #b9bbc0;
    --brand-blue: #3d86c6;
    --band-blue-dark: #2f6fb0;
    --band-blue-light: #5fa3dd;
    --art-blue-soft: #6fb2e6;
    --art-blue-pale: #a9d4f4;
    --strip-navy: #24486f;
    --strip-navy-dark: #1a3554;
    --mineral-green: #9cc63b;
    --mineral-green-dark: #7fae22;
    --white: #ffffff;
  }
  * { margin: 0; padding: 0; box-sizing: border-box; }
  html, body {
    width: 1200px;
    height: 825px;
    overflow: hidden;
    background: var(--canvas-bg);
    font-family: "Roboto", Arial, sans-serif;
  }
  .label {
    position: absolute;
    left: 60px;
    top: 110px;
    width: 1080px;
    height: 605px;
    border-radius: 6px;
    overflow: hidden;
    box-shadow: 0 10px 30px rgba(0,0,0,0.12);
  }
  .label__brand {
    position: absolute;
    inset: 0 0 auto 0;
    height: 300px;
    background: linear-gradient(180deg, var(--silver-light) 0%, var(--silver-mid) 70%, var(--silver-dark) 100%);
    display: flex;
    align-items: center;
    justify-content: center;
  }
  .brand-name {
    font-weight: 900;
    font-size: 110px;
    letter-spacing: -1px;
    color: var(--brand-blue);
    text-transform: uppercase;
    line-height: 1;
    white-space: nowrap;
  }
  .label__band {
    position: absolute;
    left: 0; right: 0;
    top: 300px;
    height: 230px;
    background: linear-gradient(100deg, var(--band-blue-dark) 0%, var(--brand-blue) 45%, var(--band-blue-light) 100%);
    border-top: 3px solid var(--silver-dark);
  }
  .claims {
    position: absolute;
    left: 70px;
    top: 58px;
    color: var(--white);
    font-size: 46px;
    line-height: 1.2;
    letter-spacing: 0.5px;
    white-space: nowrap;
  }
  .claims strong { font-weight: 700; }
  .claims span { font-weight: 300; }
  .muscle-art {
    position: absolute;
    left: 600px;
    top: 0;
    width: 190px;
    height: 227px;
    background: linear-gradient(180deg, var(--art-blue-pale) 0%, var(--art-blue-soft) 55%, var(--band-blue-light) 100%);
    opacity: 0.85;
  }
  .mineral-tile {
    position: absolute;
    left: 800px;
    top: 38px;
    width: 150px;
    height: 150px;
    border-radius: 10px;
    background: linear-gradient(160deg, var(--mineral-green) 0%, var(--mineral-green-dark) 100%);
    border: 3px solid rgba(255,255,255,0.55);
    color: var(--white);
  }
  .mineral-tile__number {
    position: absolute;
    left: 14px; top: 10px;
    font-size: 22px;
    font-weight: 400;
  }
  .mineral-tile__symbol {
    position: absolute;
    left: 0; right: 0; top: 36px;
    text-align: center;
    font-size: 62px;
    font-weight: 400;
    line-height: 1;
  }
  .mineral-tile__name {
    position: absolute;
    left: 0; right: 0; bottom: 14px;
    text-align: center;
    font-size: 18px;
    font-weight: 300;
  }
  .label__strip {
    position: absolute;
    left: 0; right: 0; bottom: 0;
    height: 75px;
    background: linear-gradient(180deg, var(--strip-navy) 0%, var(--strip-navy-dark) 100%);
    display: flex;
    align-items: center;
    justify-content: center;
    color: var(--white);
    font-weight: 700;
    font-size: 22px;
    letter-spacing: 4px;
    text-transform: uppercase;
  }
</style>
</head>
<body>
  <main class="label">
    <header class="label__brand">
      <h1 class="brand-name">Muscle Haven</h1>
    </header>
    <section class="label__band">
      <p class="claims"><strong>HIGH</strong><span>ABSORTION</span><br><strong>FAST</strong><span>ACTING</span></p>
      <div class="muscle-art" role="img" aria-label="Illustration of a leg muscle with a highlighted cramp point"></div>
      <div class="mineral-tile">
        <span class="mineral-tile__number">12</span>
        <span class="mineral-tile__symbol">Mg</span>
        <span class="mineral-tile__name">Magnesium</span>
      </div>
    </section>
    <footer class="label__strip">180 Capsules · Dietary Supplement</footer>
  </main>
</body>
</html>
```